Luxury Caviar Tin Label for High End Caviar Retailer

We are looking for a new caviar label design. We want something unique, preferably black and gold or dark blue and gold. We want a modern and luxurious feel. We have several types of caviar so we need to be able to change the name of the caviar when we print the labels. See inspiration attached. Logo is also attached. More about us: velmoronfare.com

Industry/Entity Type

fine foods industry, caviar

Font styles to use
Serif
Decorative

Requirements
Must have
• KT Velmoron Logo, space for caviar name
Nice to have
• black and gold, blue and gold

```html
<!DOCTYPE html>
<html lang="en">
<head>
<meta charset="utf-8">
<title>KT Velmoron Caviar – Royal Siberian Tin Label</title>
<link rel="stylesheet" href="https://fonts.googleapis.com/css2?family=Cinzel:wght@700&family=Marcellus&family=Oswald:wght@400;500&family=Pinyon+Script&display=swap">
<style>
  :root {
    --page: #ffffff;
    --label-light: #30333e;
    --label-dark: #1f2228;
    --gold-light: #e2c598;
    --gold: #c6a677;
    --gold-deep: #8a6d45;
    --ivory: #f3f1ec;
    --ink: #23252c;
  }
  html, body {
    margin: 0;
    width: 1200px;
    height: 1200px;
    overflow: hidden;
    background: var(--page);
  }
  .canvas {
    display: block;
    width: 1200px;
    height: 1200px;
  }
  .brand-name {
    font-family: "Marcellus", serif;
    font-size: 84px;
    letter-spacing: 3px;
    fill: url(#goldFill);
  }
  .product-type {
    font-family: "Pinyon Script", cursive;
    font-size: 104px;
    fill: url(#goldFill);
  }
  .variety-name {
    font-family: "Cinzel", serif;
    font-weight: 700;
    font-size: 82px;
    letter-spacing: 4px;
    fill: var(--ivory);
  }
  .side-note {
    font-family: "Oswald", sans-serif;
    font-size: 28px;
    fill: var(--gold);
  }
  .web-address {
    font-family: "Oswald", sans-serif;
    font-weight: 500;
    font-size: 27px;
    fill: var(--ink);
  }
  .tasting-notes {
    font-family: "Oswald", sans-serif;
    font-size: 30px;
    letter-spacing: 4px;
    fill: var(--gold);
  }
</style>
</head>
<body>
<svg class="canvas" viewBox="24 14 1932 1932" xmlns="http://www.w3.org/2000/svg">
  <defs>
    <radialGradient id="labelFill" cx="40%" cy="35%" r="75%">
      <stop offset="0" stop-color="var(--label-light)"/>
      <stop offset="1" stop-color="var(--label-dark)"/>
    </radialGradient>
    <linearGradient id="goldFill" x1="0" y1="0" x2="1" y2="1">
      <stop offset="0" stop-color="var(--gold-deep)"/>
      <stop offset="0.45" stop-color="var(--gold-light)"/>
      <stop offset="1" stop-color="var(--gold-deep)"/>
    </linearGradient>
    <linearGradient id="rule" x1="0" y1="0" x2="1" y2="0">
      <stop offset="0" stop-color="var(--gold)" stop-opacity="0"/>
      <stop offset="0.5" stop-color="var(--gold-light)"/>
      <stop offset="1" stop-color="var(--gold)" stop-opacity="0"/>
    </linearGradient>
    <path id="notesArc" d="M 542 980 A 448 448 0 0 0 1438 980"/>
  </defs>

  <g class="label">
    <circle class="label-disc" cx="990" cy="980" r="548" fill="url(#labelFill)"/>

    <g class="border-frame" fill="none">
      <circle cx="990" cy="980" r="522" stroke="url(#goldFill)" stroke-width="3"/>
      <circle cx="990" cy="980" r="502" stroke="url(#goldFill)" stroke-width="10"
              stroke-linecap="round" stroke-dasharray="0 20.5"/>
      <circle cx="990" cy="980" r="484" stroke="url(#goldFill)" stroke-width="3"/>
      <circle cx="990" cy="980" r="472" stroke="url(#goldFill)" stroke-width="1.5"/>
    </g>

    <rect class="crest" role="img" aria-label="Heraldic crest with shield and scrollwork"
          x="735" y="555" width="525" height="265" rx="60"
          fill="url(#goldFill)" opacity="0.35"/>

    <text class="brand-name" x="994" y="905" text-anchor="middle">KT VELMORON</text>

    <circle cx="810" cy="1020" r="6" fill="url(#goldFill)"/>
    <text class="product-type" x="1010" y="1035" text-anchor="middle">Caviar</text>
    <circle cx="1213" cy="1018" r="6" fill="url(#goldFill)"/>

    <text class="side-note" x="655" y="1000" text-anchor="middle">Keep Refrigerated</text>
    <text class="side-note" x="655" y="1046" text-anchor="middle">F 28-34</text>
    <text class="side-note" x="1347" y="990" text-anchor="middle">Ingredients:</text>
    <text class="side-note" x="1347" y="1036" text-anchor="middle">caviar-salt</text>

    <rect class="divider" x="828" y="1086" width="338" height="3" fill="url(#rule)"/>

    <text class="variety-name" x="998" y="1195" text-anchor="middle">ROYAL SIBERIAN</text>

    <g class="web-badge">
      <rect x="843" y="1242" width="310" height="36" rx="18" fill="url(#goldFill)"/>
      <text class="web-address" x="998" y="1270" text-anchor="middle">▪ www.velmoronfare.com ▪</text>
    </g>

    <text class="tasting-notes">
      <textPath href="#notesArc" startOffset="50%" text-anchor="middle">FARM-RAISED | SUBTLE AND DELICATE | TEXTURE: FIRM</textPath>
    </text>

    <rect class="flourish" role="img" aria-label="Small decorative flourish"
          x="962" y="1310" width="70" height="60" rx="14"
          fill="url(#goldFill)" opacity="0.5"/>
  </g>
</svg>
</body>
</html>
```